Online Advice via Video Site requires Cutting Edge Homepage

We need a creative new and exciting webdesign for our tutoring via video-chat website.

We have prepared a "demo" homepage for you to see various promotional material that we think would be suitable for the homepage. http://www.learnvista.example/demo

The actual site is undergoing some final tinkering but can be accessed and used at http://www.learnvista.example

There is NO NEED to take any colours or design structure from this.

We expect the logo to be changed to match the new site. The new logo should match the site's function.

I have included some other projects that we like the look of:
http://www.artmarketplace.example/design/143762
http://www.artmarketplace.example/design/561630
http://www.artmarketplace.example/design/247199
http://www.artmarketplace.example/design/255195
http://www.boldfinch.example/

Target Market(s)

People that will work as tutors/advisers or be student/clients

Industry/Entity Type

Tutoring

Requirements
Must have
• The search is the main feature of the homepage

After the search the next goal of the page is to get people to sign up to the site

Login, (optional inclusion of the chatterly login - if you don't include it then you need only have a "login" button... no username or password input fields)

Footer
Nice to have
• The promotional material for the site, the colours on the Slydo file CAN BE changed to suit the new design you propose.

```html
<!DOCTYPE html>
<html lang="en">
<head>
<meta charset="utf-8">
<title>LearnVista — Home</title>
<link href="https://fonts.googleapis.com/css2?family=Arimo:wght@400;700&family=Cinzel:wght@400;600&family=Tinos:wght@400;700&display=swap" rel="stylesheet">
<style>
:root{
  --ink:#2b2b2b;
  --topbar:#2a2c2e;
  --sky-deep:#2f86c6;
  --sky-light:#cfe9f8;
  --orange:#f7a01c;
  --orange-dark:#e07f06;
  --steel:#3d7ea6;
  --steel-dark:#1f5676;
  --hero:#5e5e5e;
  --hero-dark:#474747;
  --tab:#4b4b4b;
  --accent-blue:#1d7fc4;
  --red:#e4252a;
  --panel:#f1f1f1;
  --panel-line:#d8d8d8;
  --muted:#777;
  --footer:#2c2d2f;
}
*{box-sizing:border-box;margin:0;padding:0}
html,body{width:1050px;height:1200px;overflow:hidden}
body{position:relative;background:#f4f4f4;font-family:"Arimo",Arial,sans-serif;color:var(--ink)}
.abs{position:absolute}

/* top bar */
.topbar{left:0;top:0;width:1050px;height:43px;background:linear-gradient(#3a3c3f,var(--topbar));border-bottom:1px solid #111}
.field{height:25px;border-radius:5px;background:linear-gradient(#2a2b2d,#45474a);border:1px solid #5a5c5f;color:#e8e8e8;font-size:12px;padding:5px 14px}
.field.name{left:480px;top:10px;width:173px}
.field.pass{left:666px;top:10px;width:172px}
.login{left:857px;top:11px;width:74px;height:23px;border-radius:4px;background:linear-gradient(#4e90b8,var(--steel-dark));color:#fff;font-size:13px;text-align:center;line-height:23px;box-shadow:0 1px 2px #000}

/* header */
.header{left:0;top:43px;width:1050px;height:290px;background:radial-gradient(ellipse 380px 150px at 560px 110px,#f2fbff 0%,var(--sky-light) 30%,rgba(120,190,235,.9) 60%,transparent 100%),linear-gradient(var(--sky-deep) 0%,#7cc0ea 45%,#e7f3fb 75%,#f4f4f4 100%)}
.brand{left:70px;top:122px;display:flex;align-items:center;gap:10px}
.brand-mark{width:18px;height:18px;background:#fff}
.brand-name{font-family:"Arimo",Arial,sans-serif;font-size:30px;font-weight:400;color:#fff}
.search-label{left:299px;top:104px;font-size:12px;color:#fff;letter-spacing:.2px}
.search-label b{font-weight:700}
.search-input{left:300px;top:124px;width:356px;height:37px;border-radius:4px;background:linear-gradient(#d9d9d9,#fff 40%);border:1px solid #9aa;box-shadow:inset 0 2px 4px rgba(0,0,0,.35);font-style:italic;font-size:12px;color:#8a8a8a;padding:11px 18px}
.search-btn{left:665px;top:124px;width:202px;height:35px;border-radius:5px;background:linear-gradient(#ffc04d,var(--orange) 50%,var(--orange-dark));color:#fff;font-size:15px;text-align:center;line-height:35px;box-shadow:0 2px 4px rgba(0,0,0,.25)}

/* nav */
.nav{left:97px;top:246px;width:852px;height:72px;display:flex;background:linear-gradient(#f4f4f4,#dcdcdc);border:1px solid #bfc6cc;border-bottom:2px solid #7ab5d6;border-radius:3px;box-shadow:0 12px 24px rgba(0,0,0,.12)}
.nav-item{text-align:center;padding-top:16px;border-right:1px solid #b9b9b9;font-family:"Cinzel",serif}
.nav-item:last-child{border-right:none}
.nav-item .title{display:block;font-size:17px;color:#333;letter-spacing:1px}
.nav-item .sub{display:block;font-size:10px;color:#666;margin-top:3px;letter-spacing:.5px}
.nav-item.active{background:linear-gradient(#6e6e6e,#4a4a4a)}
.nav-item.active .title{color:#fff}
.nav-item.active .sub{color:#ddd}

/* hero */
.hero{left:97px;top:341px;width:852px;height:277px;background:linear-gradient(90deg,var(--hero-dark),var(--hero) 40%,#6a6a6a)}
.photo-back{left:152px;top:357px;width:330px;height:245px;background:#d89a2e;border:5px solid #fff;box-shadow:0 3px 8px rgba(0,0,0,.5)}
.photo{left:168px;top:348px;width:326px;height:257px;background:linear-gradient(120deg,#ede8e2,#c9a992 45%,#f5f5f5);border:6px solid #fff;transform:rotate(2deg);box-shadow:0 4px 10px rgba(0,0,0,.55)}
.hero-title{left:518px;top:370px;font-size:24px;color:#fff;letter-spacing:.3px}
.hero-title em{font-style:normal;color:var(--red)}
.bullets{top:411px;list-style:none;font-size:12px}
.bullets li{height:28px;padding-left:15px;position:relative;color:#fff}
.bullets li::before{content:"";position:absolute;left:0;top:4px;width:8px;height:8px;border-radius:50%;background:#cfcfcf}
.bullets li.dim{color:#c8c8c8}
.bullets.left{left:538px}
.bullets.right{left:730px}
.hero-rule{left:500px;top:515px;width:406px;height:1px;background:#3e3e3e;border-bottom:1px solid #7a7a7a}
.cta{left:518px;top:526px;width:180px;height:35px;border-radius:3px;background:linear-gradient(#5d9cc0,var(--steel-dark));color:#fff;font-size:15px;text-align:center;line-height:35px;box-shadow:0 2px 4px rgba(0,0,0,.5)}
.hero-note{left:520px;top:566px;width:390px;font-size:12px;line-height:16px;color:#111}

/* tabs */
.tabs{left:97px;top:618px;width:852px;height:71px;display:flex;background:linear-gradient(#585858,#3e3e3e)}
.tab{position:relative;display:flex;align-items:center;gap:10px;padding-left:20px;border-right:1px solid #2f2f2f}
.tab:last-child{border-right:none}
.tab .label{font-size:18px;color:#2c2c2c;line-height:18px}
.tab .hint{font-size:10px;color:#3b3b3b}
.tab.active .label{color:var(--accent-blue)}
.tab.active .hint{color:#fff}
.tab.active::after{content:"";position:absolute;left:80px;bottom:0;border:7px solid transparent;border-bottom-color:var(--accent-blue)}
.strip{left:97px;top:689px;width:852px;height:12px;background:linear-gradient(#2b86c4,#145a8a)}
.strip-shadow{left:97px;top:701px;width:852px;height:26px;background:radial-gradient(ellipse 430px 14px at 50% 0,rgba(0,0,0,.45),transparent)}

/* videos */
.videos{left:98px;top:738px;width:636px;height:405px;background:var(--panel);border:1px solid var(--panel-line)}
.video-card{top:745px;width:298px;height:390px;background:#fff;border:1px solid #cfcfcf}
.video-card.advisors{left:109px}
.video-card.students{left:419px}
.video-head{height:26px;background:linear-gradient(#e4e4e4,#d0d0d0);font-family:"Tinos",serif;font-size:15px;color:#333;padding:5px 11px;text-transform:uppercase}
.video-head b{color:#111;font-weight:400}
.video-frame{position:absolute;left:4px;top:31px;width:288px;height:290px}
.advisors .video-frame{background:linear-gradient(100deg,#e7c35c,#6b5a4a 40%,#3c3532 70%,#9b8b7e)}
.students .video-frame{background:linear-gradient(180deg,#111 0 10%,#d8dde0 10%,#7a6a5a 45%,#e9e4d8 80%)}
.player-bar{position:absolute;left:4px;top:321px;width:288px;height:25px;background:linear-gradient(#2c2c2c,#0e0e0e)}
.play-btn{position:absolute;left:100px;top:115px;width:78px;height:60px;border-radius:6px;background:rgba(255,255,255,.25)}
.time{position:absolute;left:83px;top:7px;font-size:9px;color:#fff}
.more{position:absolute;right:0;top:356px;width:92px;height:21px;border-radius:3px;background:linear-gradient(#5f9dc2,var(--steel-dark));color:#fff;font-family:"Tinos",serif;font-size:12px;text-align:center;line-height:21px}

/* sidebar */
.side-head{left:742px;width:199px;height:37px;border:3px solid #cfcfcf;border-radius:6px;background:#fff;font-family:"Tinos",serif;font-size:16px;color:#333;padding:6px 12px}
.side-head.topics{top:739px}
.side-head.testi{top:935px;display:flex;justify-content:space-between;align-items:center}
.arrows{display:flex;gap:4px}
.arrows span{width:16px;height:16px;border-radius:50%;background:#333}
.topics-list{left:763px;top:788px;list-style:none;font-size:12px;color:#555}
.topics-list li{height:22.7px;padding-left:17px;position:relative}
.topics-list li::before{content:"";position:absolute;left:2px;top:4px;width:5px;height:5px;border-radius:50%;background:#222}
.quote{left:757px;top:983px;width:180px;font-size:10.5px;line-height:18.4px;color:#666;text-align:justify}
.quote .mark{font-family:"Tinos",serif;font-size:28px;font-weight:700;color:#444;float:left;line-height:18px;margin-right:8px;margin-top:4px}
.quote-by{left:820px;top:1140px;width:117px;text-align:right;font-size:12px;color:#666}
.quote-by b{color:#333;font-weight:400}

/* footer */
.footer{left:0;top:1158px;width:1050px;height:42px;background:var(--footer);font-size:9.5px;color:#aaa;padding:16px 20px}
</style>
</head>
<body>

<div class="abs topbar"></div>
<div class="abs field name">name</div>
<div class="abs field pass">password</div>
<div class="abs login">LOG IN</div>

<header class="abs header"></header>
<div class="abs brand"><span class="brand-mark"></span><span class="brand-name">LearnVista</span></div>
<div class="abs search-label">SEARCH <b>LEARNVISTA</b>'S TOPICS &amp; ADVISORS</div>
<div class="abs search-input">type text here . . .</div>
<div class="abs search-btn">search topics &amp; advisors</div>

<nav class="abs nav">
  <div class="nav-item active" style="width:123px"><span class="title">HOME</span><span class="sub">OUR SITE</span></div>
  <div class="nav-item" style="width:159px"><span class="title">SERVICES</span><span class="sub">WHAT WE OFFER?</span></div>
  <div class="nav-item" style="width:194px"><span class="title">INSTRUCTORS</span><span class="sub">WHO ARE THEY?</span></div>
  <div class="nav-item" style="width:171px"><span class="title">ABOUT US</span><span class="sub">WHO WE ARE?</span></div>
  <div class="nav-item" style="width:203px"><span class="title">CONTACT US</span><span class="sub">(555) 010.2468</span></div>
</nav>

<section class="abs hero"></section>
<div class="abs photo-back"></div>
<div class="abs photo" role="img" aria-label="Photo of a stressed man holding his head in thought"></div>
<h1 class="abs hero-title">LET YOUR <em>PROBLEMS</em> BE SOLVE</h1>
<ul class="abs bullets left">
  <li>Approach the issue with clarity</li>
  <li class="dim">Understand the issue</li>
  <li>Understand the issue</li>
  <li class="dim">Plan a strategy</li>
</ul>
<ul class="abs bullets right">
  <li>Execute your strategy</li>
  <li class="dim">Evaluate the results</li>
  <li>Continue to evaluate and execute</li>
</ul>
<div class="abs hero-rule"></div>
<div class="abs cta">CONTACT NOW</div>
<p class="abs hero-note">Always try to remain calm and logical when approaching a problem, resolution ultimately lies in this approach.</p>

<div class="abs tabs">
  <div class="tab" style="width:186px">
    <svg width="32" height="44" viewBox="0 0 32 44"><text x="2" y="38" font-family="Arimo,Arial,sans-serif" font-weight="700" font-size="44" fill="#2a2a2a">?</text></svg>
    <div><div class="label">QUESTIONS</div><div class="hint">need an answer, click here</div></div>
  </div>
  <div class="tab active" style="width:203px">
    <svg width="30" height="36" viewBox="0 0 30 36"><path d="M28 2 L2 20 L28 34 Z" fill="#1d7fc4"/></svg>
    <div><div class="label">DIRECT</div><div class="hint">point out problems</div></div>
  </div>
  <div class="tab" style="width:223px">
    <svg width="42" height="40" viewBox="0 0 42 40"><path d="M2 22 L10 16 L17 26 L38 2 L41 6 L17 38 Z" fill="#2a2a2a"/></svg>
    <div><div class="label">CHECK</div><div class="hint">solve appropriately</div></div>
  </div>
  <div class="tab" style="width:240px;padding-left:30px">
    <svg width="40" height="40" viewBox="0 0 40 40"><circle cx="20" cy="20" r="18" fill="none" stroke="#2a2a2a" stroke-width="3"/><circle cx="20" cy="20" r="11" fill="none" stroke="#2a2a2a" stroke-width="3"/><circle cx="20" cy="20" r="4" fill="#2a2a2a"/></svg>
    <div><div class="label">TARGET</div><div class="hint">aim your goals now</div></div>
  </div>
</div>
<div class="abs strip"></div>
<div class="abs strip-shadow"></div>

<section class="abs videos"></section>
<div class="abs video-card advisors">
  <div class="video-head">Videos for <b>advisors</b></div>
  <div class="video-frame" role="img" aria-label="Video still of a woman and a man in a business meeting at a desk"><div class="play-btn"></div></div>
  <div class="player-bar"><span class="time">00:21 / 59:32</span></div>
  <div class="more">more videos</div>
</div>
<div class="abs video-card students">
  <div class="video-head">Videos for <b>students</b></div>
  <div class="video-frame" role="img" aria-label="Video still of a student writing in a binder in a classroom"><div class="play-btn"></div></div>
  <div class="player-bar"><span class="time">00:21 / 59:32</span></div>
  <div class="more">more videos</div>
</div>

<div class="abs side-head topics">Advisors by Topics</div>
<ul class="abs topics-list">
  <li>English</li><li>Building</li><li>Cultural Studies</li><li>Criminology</li><li>Agriculture</li><li>Veterinary Science</li>
</ul>
<div class="abs side-head testi">Testimonials<span class="arrows"><span></span><span></span></span></div>
<p class="abs quote"><span class="mark">&ldquo;</span>Fusce dapibus, tellus ac cursus commodo, tortor mauris condimentum nibh, ut fermentum massa justo sit amet risus. Cras mattis consectetur purus sit amet fermentum. Maecenas faucibus mollis interdum. Cras justo odio, dapibus ac facilisis in, egestas eget quam.</p>
<div class="abs quote-by"><b>Dorvane</b>, Artist</div>

<footer class="abs footer">t: 1-555-014-0199 &nbsp;e: info@learnvista.example</footer>

</body>
</html>
```